2024 Veltmore Financial Team Deck

I have created a power point slide deck and I need the slide deck recreated. Organized, with better color, background pictures, etc. I am thinking the colors for the presentation can be navy blue, and white, and gold, with hints of silver and black. We are financial planning firm that specializes in working with tech companies in silicon valley.

```html
<!DOCTYPE html>
<html lang="en">
<head>
<meta charset="utf-8">
<title>Veltmore Financial 2024 Team Deck</title>
<link rel="stylesheet" href="https://fonts.googleapis.com/css2?family=Oswald:wght@500;600;700&family=Roboto:wght@400;500;700&display=swap">
<style>
:root{
  --navy:#0a0a82;
  --gold:#d2ae39;
  --cream:#fbf1d2;
  --ink:#111111;
  --text:#3d3d3d;
  --muted:#7a7a7a;
  --stage:#8d8d8d;
  --white:#ffffff;
}
*{margin:0;padding:0;box-sizing:border-box}
html,body{width:1200px;height:3976px;overflow:hidden;background:var(--stage)}
body{position:relative;font-family:"Roboto",Arial,sans-serif;color:var(--text)}
.slide{position:absolute;left:85px;width:1030px;height:580px;overflow:hidden;background:var(--white)}
.s1{top:93px}.s2{top:735px}.s3{top:1378px}.s4{top:2020px}.s5{top:2662px}.s6{top:3305px}
.abs{position:absolute}
.heading{font-family:"Oswald",Impact,sans-serif;font-weight:700;text-transform:uppercase;letter-spacing:.2px;line-height:1}
.navy{color:var(--navy)}

/* slide 1 */
.hero-photo{position:absolute;inset:0;background:radial-gradient(circle at 10% 5%,#f2c6c2 0,#efe6ea 18%,transparent 40%),linear-gradient(120deg,#f2f1f4 0%,#dfe2e8 45%,#a9b3c2 75%,#7d8797 100%)}
.hero-circle{position:absolute;left:65px;top:57px;width:442px;height:442px;border-radius:50%;background:var(--white);display:flex;flex-direction:column;align-items:center;justify-content:center;text-align:center}
.hero-circle .welcome{font-size:36px;color:var(--navy);margin-bottom:14px}
.hero-circle .firm{font-size:50px;color:var(--ink);line-height:1.08}

/* shared corner backgrounds */
.bg-gold{background:var(--gold)}
.panel-round{position:absolute;top:0;right:0;bottom:0;border-top-left-radius:140px}
.photo{position:absolute;border-radius:26px}

/* slide 2 */
.s2 .panel-round{left:205px;background:var(--navy)}
.s2 .photo{left:60px;top:133px;width:443px;height:377px;background:linear-gradient(135deg,#7f8a86 0%,#b9b4a4 40%,#6f6a62 70%,#3e3c3a 100%)}
.mission-title{left:293px;top:44px;font-size:40px;color:var(--white)}
.firm-right{right:65px;top:47px;font-size:34px}
.s2 .firm-right{color:var(--white)}
.mission-body{left:550px;top:124px;width:430px;color:var(--white);font-size:13px;line-height:1.55}
.mission-body .lead{font-weight:700;font-size:13.5px;line-height:2.25;margin-bottom:4px}
.mission-body p{margin-bottom:10px}
.mission-body .how{font-weight:700;margin-bottom:8px}
.check-list{list-style:none}
.check-list li{position:relative;padding-left:22px;margin-bottom:10px}
.check-list li svg{position:absolute;left:0;top:4px;width:12px;height:12px}

/* slide 3 */
.s3{background:var(--gold)}
.s3 .white-left{position:absolute;left:0;top:0;bottom:0;width:819px;background:var(--white);border-top-right-radius:150px}
.s3 .firm-left{left:60px;top:47px;font-size:34px}
.vision-title{left:527px;top:44px;font-size:40px;color:var(--ink);display:flex;align-items:baseline;gap:14px}
.vision-title small{font-family:"Roboto",Arial,sans-serif;font-weight:700;font-size:19px;text-transform:none}
.s3 .photo{left:520px;top:131px;width:445px;height:379px;border-radius:22px 22px 48px 22px;background:linear-gradient(140deg,#5b5f66 0%,#9aa1aa 35%,#d7d9dc 55%,#6d6f73 80%,#2f3135 100%)}
.vision-list{position:absolute;left:63px;top:108px;width:433px;list-style:none;font-size:9.6px;line-height:1.55;color:#555;text-align:justify}
.vision-list li{position:relative;padding-left:26px;margin-bottom:6px}
.vision-list li svg{position:absolute;left:0;top:50%;margin-top:-6px;width:12px;height:12px}

/* slide 4 */
.s4{background:var(--navy)}
.s4 .gold-edge{position:absolute;left:0;top:0;bottom:0;width:860px;background:var(--gold);border-radius:0 50px 50px 0}
.s4 .cream-panel{position:absolute;left:0;top:0;bottom:0;width:852px;background:var(--cream);border-radius:0 46px 46px 0}
.org-title{left:62px;top:47px;font-size:34px;color:var(--ink)}
.s4 .firm-right{right:200px;left:auto;color:var(--ink)}
.org-lines{position:absolute;left:0;top:0}
.president{position:absolute;left:151px;top:248px;width:180px;height:180px;border-radius:50%;background:var(--white);display:flex;flex-direction:column;align-items:center;justify-content:center;gap:6px}
.president b{font-size:17px;font-weight:500;color:var(--ink)}
.president span{font-size:14px;color:var(--muted)}
.role-box{position:absolute;left:473px;width:233px;height:72px;background:var(--white);padding:12px 0 0 26px;box-shadow:0 2px 6px rgba(0,0,0,.06)}
.role-box b{display:block;font-size:15.5px;font-weight:500;color:var(--ink);line-height:1.2}
.role-box span{display:block;font-size:14px;color:var(--muted);margin-top:4px}
.role-box.two{padding-top:6px}
.role-box.two span{margin-top:1px}

/* slides 5 & 6 */
.s5,.s6{background:var(--gold)}
.s5 .panel-round,.s6 .panel-round{left:205px;background:var(--white)}
.s5 .firm-right,.s6 .firm-right{top:62px}
.vital-title{left:259px;top:118px;font-size:34px;color:var(--ink)}
.vital-desc{left:259px;top:183px;width:690px;font-size:13px;line-height:1.6;color:var(--ink)}
.fn-card{position:absolute;top:244px;width:222px;height:255px;background:var(--white);transform:skewX(-3deg);box-shadow:0 4px 14px rgba(0,0,0,.18)}
.fn-inner{transform:skewX(3deg);padding:20px 18px 0 28px}
.fn-icon{display:block;margin:0 auto;width:60px;height:60px}
.fn-name{text-align:center;font-weight:700;font-size:14px;color:var(--ink);margin-top:2px}
.fn-rule{width:30px;height:2px;background:var(--navy);margin:8px auto 22px}
.fn-list{list-style:none;font-size:12.4px;color:#555;line-height:1.3}
.fn-list li{position:relative;padding-left:21px;margin-bottom:14px}
.fn-list li svg{position:absolute;left:0;top:2px;width:12px;height:12px}
.fn-arrow{position:absolute;right:14px;bottom:0;width:26px;height:26px;display:flex;align-items:center;justify-content:center}

.source-title{left:0;right:0;padding-left:205px;top:133px;text-align:center;font-size:34px;color:var(--ink)}
.source-card{position:absolute;top:208px;width:253px;height:309px;background:var(--white);border-radius:18px;border:2px solid #f1e8c8;box-shadow:0 0 0 5px #fff,0 0 0 7px #f1e8c8,0 4px 16px rgba(0,0,0,.12);padding:68px 0 0 27px}
.source-card .num{font-family:"Oswald",Impact,sans-serif;font-weight:600;font-size:34px;color:var(--navy);line-height:1}
.source-card .label{font-family:"Oswald",Impact,sans-serif;font-weight:600;font-size:28px;color:var(--ink);line-height:1;margin:12px 0 20px}
.source-card ul{list-style:none;font-size:12.6px;font-weight:700;color:var(--ink)}
.source-card li{position:relative;padding-left:23px;margin-bottom:18px}
.source-card li svg{position:absolute;left:0;top:1px;width:13px;height:13px}
</style>
</head>
<body>
<svg width="0" height="0" style="position:absolute">
  <defs>
    <symbol id="tick" viewBox="0 0 12 12"><circle cx="6" cy="6" r="6" fill="currentColor"/><path d="M3.2 6.2 5.2 8.1 8.9 4.1" fill="none" stroke="#fff" stroke-width="1.6" stroke-linecap="round" stroke-linejoin="round"/></symbol>
  </defs>
</svg>

<!-- Title -->
<section class="slide s1">
  <div class="hero-photo" role="img" aria-label="Photo of a hand with a pen working on a calculator at a bright desk"></div>
  <div class="hero-circle">
    <div class="heading welcome">Welcome to</div>
    <div class="heading firm">Veltmore Financial<br>2024</div>
  </div>
</section>

<!-- Mission -->
<section class="slide s2 bg-gold">
  <div class="panel-round"></div>
  <div class="photo" role="img" aria-label="Photo of advisors smiling around a meeting table in a bright office"></div>
  <h2 class="abs heading mission-title">Our Mission</h2>
  <h2 class="abs heading firm-right">Veltmore Financials</h2>
  <div class="abs mission-body">
    <div class="lead">TO PROVIDE OUR CLIENT WITH THE SYSTEMS<br>AND PROCESSES NEEDED TO GUIDE THEIR HERO'S<br>JOURNEY AND LEAVE AN IMPACT</div>
    <p>The Hero's Journey: We believe everyone has a purpose, God's purpose in their life, and it is our mission to help our clients relentlessly pursue their purpose. A life with purpose is a life living out your Hero's Journey!</p>
    <div class="how">HOW</div>
    <ul class="check-list" style="color:var(--white)">
      <li><svg><use href="#tick"/></svg>Our financial planning &amp; wealth management services give our clients</li>
      <li><svg><use href="#tick"/></svg>More Time &amp; Clarity on their plan and what is needed to accomplish the objective</li>
      <li><svg><use href="#tick"/></svg>We help our clients think bigger and professionally hold them accountable to their goals</li>
      <li><svg><use href="#tick"/></svg>We help reduce taxes drag , increase diversification, reduce investment risk, &amp; maximize investment returns so that our clients have the financial resources to maximize their potential and ultimately have a larger Impact on the world.</li>
    </ul>
  </div>
</section>

<!-- Vision -->
<section class="slide s3">
  <div class="white-left"></div>
  <h2 class="abs heading navy firm-left">Veltmore Financials</h2>
  <h2 class="abs heading vision-title">Firm Vision <small>(December 2026)</small></h2>
  <ul class="vision-list" style="color:#555">
    <li><svg style="color:var(--gold)"><use href="#tick"/></svg>We are an elite wealth management firm at Harborline Mutual, that is impact driven and focused on the clients' goals, needs, and objectives above all else. We specialize in serving Executives, Directors, &amp; Vice Presidents at Arcwell, Quorra, Lumenta, &amp; other tech companies where a heavy part of compensation is coming in the form of stock (RSU/ESPP).</li>
    <li><svg style="color:var(--gold)"><use href="#tick"/></svg>Over the last 3 years we have grown the firm organically, through introductions, and seminars/speaking events.</li>
    <li><svg style="color:var(--gold)"><use href="#tick"/></svg>We are the primary advisory firm &amp; financial planning relationship for 300 households in this space. We manage over $150m in assets and our minimize account size has grown to $500k. We are consistently qualifying for forum and this year (awards year 2026) we will have $1M premium and $1M GDC in just 8 years at Harborline Mutual.</li>
    <li><svg style="color:var(--gold)"><use href="#tick"/></svg>Our team has 3 lead advisors that are each fully responsible for servicing a sleeve of 80 – 125 clients on an annual basis. Each advisor is also responsible for bringing on an additional $6M of AUM annually, 10 new clients, and writing $150k of premium.</li>
    <li><svg style="color:var(--gold)"><use href="#tick"/></svg>Our team has a mandatory team trip every year, we don't work weekends, we rarely work past 5pm, and we have frogman Fridays. Every Friday the team is off by 1pm at the latest, we get in, get the work done, and get out.</li>
    <li><svg style="color:var(--gold)"><use href="#tick"/></svg>Daniel is only taking client meetings 4 days/week and takes no more then 16 on any given week. He has a 2nd chair in every meeting that is taking notes and will be responsible for the follow up. The calendar is filled by the lead advisors who are working on a path to partnership at the firm. Everyone is financially tied to bottom line revenue. We have a team of winners!</li>
    <li><svg style="color:var(--gold)"><use href="#tick"/></svg>We are healthy, fit, &amp; happy. We have the opportunity to help who we want when we want. We have control over our lives and work schedule. We dictate the pace and cadence that we want to move at based on our goals any given year. Every member of the team loves the team, supports the mission, and wants to leave an impact.</li>
    <li><svg style="color:var(--gold)"><use href="#tick"/></svg>We are well on our way to managing $1B by December 2033</li>
  </ul>
  <div class="photo" role="img" aria-label="Photo of colleagues reviewing printed charts with pens at a conference table"></div>
</section>

<!-- Org chart -->
<section class="slide s4">
  <div class="gold-edge"></div>
  <div class="cream-panel"></div>
  <h2 class="abs heading org-title">Future Org Chart</h2>
  <h2 class="abs heading firm-right">Veltmore Financials</h2>
  <svg class="org-lines" width="1030" height="580" viewBox="0 0 1030 580" aria-hidden="true">
    <circle cx="241" cy="338" r="108" fill="none" stroke="var(--navy)" stroke-width="2" stroke-dasharray="2 3"/>
    <circle cx="241" cy="338" r="98" fill="#f3e4b8"/>
    <g fill="none" stroke="var(--navy)" stroke-width="2">
      <path d="M332 240V175H398"/>
      <path d="M332 430V488H398"/>
      <path d="M355 281H417"/>
      <path d="M355 384H417"/>
    </g>
    <g fill="var(--navy)">
      <circle cx="445" cy="175" r="5"/><circle cx="445" cy="281" r="5"/>
      <circle cx="445" cy="384" r="5"/><circle cx="445" cy="488" r="5"/>
    </g>
  </svg>
  <div class="president"><b>President</b><span>Daniel Whitmore</span></div>
  <div class="role-box" style="top:139px"><b>Private Wealth Advisor</b><span>(GRU)</span></div>
  <div class="role-box two" style="top:245px"><b>Director of Insurance &amp;<br>Office Manager</b><span>Claire</span></div>
  <div class="role-box two" style="top:348px"><b>Director of Investments &amp;<br>Planning</b><span>Moreno</span></div>
  <div class="role-box" style="top:452px"><b>COO</b><span>Evan Calloway</span></div>
</section>

<!-- Vital functions -->
<section class="slide s5">
  <div class="panel-round"></div>
  <h2 class="abs heading navy firm-right">Veltmore Financials</h2>
  <h2 class="abs heading vital-title">Vital Functions</h2>
  <p class="abs vital-desc">These are 3 vital functions on the leverage curve that you need to drive massive results and make it rain. Like Marcus Vale say's if we can focus on these 3 things and eliminate all other distractions we can accomplish anything!</p>

  <div class="fn-card" style="left:66px">
    <div class="fn-inner">
      <svg class="fn-icon" viewBox="0 0 60 60" aria-hidden="true"><g fill="var(--navy)"><rect x="28" y="4" width="4" height="8"/><circle cx="30" cy="5" r="4"/><rect x="12" y="12" width="36" height="28" rx="8"/><rect x="6" y="20" width="5" height="12" rx="2"/><rect x="49" y="20" width="5" height="12" rx="2"/><rect x="22" y="42" width="16" height="10" rx="3"/></g><circle cx="23" cy="26" r="5" fill="#fff"/><circle cx="37" cy="26" r="5" fill="#fff"/><rect x="24" y="34" width="12" height="2" fill="#fff"/></svg>
      <div class="fn-name">Daniel</div><div class="fn-rule"></div>
      <ul class="fn-list"><li><svg style="color:var(--navy)"><use href="#tick"/></svg>Client Meeting</li><li><svg style="color:var(--navy)"><use href="#tick"/></svg>Dial</li><li><svg style="color:var(--navy)"><use href="#tick"/></svg>Business Development</li></ul>
    </div>
    <div class="fn-arrow" style="background:var(--navy)"><svg width="12" height="8" viewBox="0 0 12 8"><path d="M0 4H10M7 1 10 4 7 7" fill="none" stroke="#fff" stroke-width="1.5"/></svg></div>
  </div>

  <div class="fn-card" style="left:313px">
    <div class="fn-inner">
      <svg class="fn-icon" viewBox="0 0 60 60" aria-hidden="true"><g fill="var(--gold)"><rect x="6" y="34" width="7" height="18"/><rect x="16" y="26" width="7" height="26"/><rect x="26" y="18" width="7" height="34"/><path d="M29 2 38 12H33V16H26V12H20Z"/><circle cx="44" cy="38" r="12"/></g><text x="44" y="43" font-family="Roboto,Arial,sans-serif" font-size="14" font-weight="700" fill="#fff" text-anchor="middle">$</text></svg>
      <div class="fn-name">Moreno</div><div class="fn-rule"></div>
      <ul class="fn-list"><li><svg style="color:var(--gold)"><use href="#tick"/></svg>Investment Processing</li><li><svg style="color:var(--gold)"><use href="#tick"/></svg>Final Case Prep/Executive Summary</li><li><svg style="color:var(--gold)"><use href="#tick"/></svg>Service Existing Book</li></ul>
    </div>
    <div class="fn-arrow" style="background:var(--gold)"><svg width="12" height="8" viewBox="0 0 12 8"><path d="M0 4H10M7 1 10 4 7 7" fill="none" stroke="#fff" stroke-width="1.5"/></svg></div>
  </div>

  <div class="fn-card" style="left:533px">
    <div class="fn-inner">
      <svg class="fn-icon" viewBox="0 0 60 60" aria-hidden="true"><g fill="var(--navy)"><circle cx="14" cy="8" r="4"/><rect x="11" y="14" width="6" height="18"/><rect x="11" y="32" width="3" height="18"/><rect x="15" y="32" width="3" height="18"/><rect x="22" y="40" width="7" height="12"/><rect x="32" y="34" width="7" height="18"/><rect x="42" y="26" width="8" height="26"/><rect x="6" y="52" width="48" height="2"/></g></svg>
      <div class="fn-name">Claire</div><div class="fn-rule"></div>
      <ul class="fn-list"><li><svg style="color:var(--navy)"><use href="#tick"/></svg>Insurance Processing</li><li><svg style="color:var(--navy)"><use href="#tick"/></svg>Calendar Management for Daniel</li><li><svg style="color:var(--navy)"><use href="#tick"/></svg>OCI Manager for Daniel</li></ul>
    </div>
    <div class="fn-arrow" style="background:var(--navy)"><svg width="12" height="8" viewBox="0 0 12 8"><path d="M0 4H10M7 1 10 4 7 7" fill="none" stroke="#fff" stroke-width="1.5"/></svg></div>
  </div>

  <div class="fn-card" style="left:750px">
    <div class="fn-inner">
      <svg class="fn-icon" viewBox="0 0 60 60" aria-hidden="true"><g fill="var(--gold)"><circle cx="30" cy="18" r="12"/><path d="M8 54C8 40 18 32 30 32S52 40 52 54Z"/></g></svg>
      <div class="fn-name">Evan</div><div class="fn-rule"></div>
      <ul class="fn-list"><li><svg style="color:var(--gold)"><use href="#tick"/></svg>Activity Numbers &amp; reporting</li><li><svg style="color:var(--gold)"><use href="#tick"/></svg>Financials / Bookkeeping</li><li><svg style="color:var(--gold)"><use href="#tick"/></svg>Team Project Manger</li></ul>
    </div>
    <div class="fn-arrow" style="background:var(--gold)"><svg width="12" height="8" viewBox="0 0 12 8"><path d="M0 4H10M7 1 10 4 7 7" fill="none" stroke="#fff" stroke-width="1.5"/></svg></div>
  </div>
</section>

<!-- Where it comes from -->
<section class="slide s6">
  <div class="panel-round"></div>
  <h2 class="abs heading navy firm-right">Veltmore Financials</h2>
  <h2 class="abs heading source-title">Where does it come from?</h2>
  <div class="source-card" style="left:100px">
    <div class="num">$1M</div><div class="label">PREMIUM</div>
    <ul><li><svg style="color:var(--gold)"><use href="#tick"/></svg>New Business (Jungle): $750k</li><li><svg style="color:var(--gold)"><use href="#tick"/></svg>Existing Clients (Zoo): $150k</li><li><svg style="color:var(--gold)"><use href="#tick"/></svg>Strategic KL Partners: $100k</li></ul>
  </div>
  <div class="source-card" style="left:390px">
    <div class="num">$18M</div><div class="label">NEW AUM</div>
    <ul><li><svg style="color:var(--gold)"><use href="#tick"/></svg>New Business (Jungle): $10M</li><li><svg style="color:var(--gold)"><use href="#tick"/></svg>Existing Clients (Zoo): $4M</li><li><svg style="color:var(--gold)"><use href="#tick"/></svg>Strategic KL Partners: $4M</li></ul>
  </div>
  <div class="source-card" style="left:681px;padding-left:20px">
    <div class="num">60</div><div class="label">NEW CLIENTS</div>
    <ul><li><svg style="color:var(--gold)"><use href="#tick"/></svg>Daniel: 48</li><li><svg style="color:var(--gold)"><use href="#tick"/></svg>Moreno: 12</li></ul>
  </div>
</section>
</body>
</html>
```